6 - 8 'Holistic' Instagram Graphics

Hi there!
We are looking to build up a library of Graphic Templates to use as Instagram & Facebook posts for our Holistic Medi Spa (& 3 other companies eventually)
This competition is for a sample of 6 - 8 designs. For the winner(s), we will make an agreement for a batch order (Looking for 200+ designs in total), and will be looking to make a long term arrangement.
Please find a full job description in the attached Word Document.
Any questions, don't hesitate to ask.
Thanks!
Medical Spa

```html
<!DOCTYPE html>
<html lang="en">
<head>
<meta charset="utf-8">
<title>Natural Healing Quote Post</title>
<link rel="stylesheet" href="https://fonts.googleapis.com/css2?family=Barlow:wght@800&family=Raleway:wght@200&display=swap">
<style>
  :root {
    --bg-deep: #005a86;
    --bg-mid: #0a7db0;
    --bg-light: #1a92c4;
    --quote-top: #19f0ff;
    --quote-bottom: #00a8ff;
    --author: #44d6ff;
  }
  html, body {
    margin: 0;
    padding: 0;
    width: 1200px;
    height: 1200px;
    overflow: hidden;
    background: var(--bg-deep);
  }
  .post {
    position: relative;
    width: 1200px;
    height: 1200px;
    overflow: hidden;
  }
  .post__photo {
    position: absolute;
    inset: 0;
    background:
      radial-gradient(ellipse 40% 55% at 52% 38%, var(--bg-light) 0%, transparent 70%),
      radial-gradient(ellipse 30% 45% at 90% 30%, var(--bg-light) 0%, transparent 70%),
      linear-gradient(180deg, var(--bg-mid) 0%, var(--bg-deep) 100%);
  }
  .post__quote {
    position: absolute;
    left: 0;
    right: 0;
    top: 282px;
    margin: 0;
    text-align: center;
    font-family: "Barlow", "Arial Narrow", sans-serif;
    font-weight: 800;
    font-size: 92px;
    line-height: 98px;
    letter-spacing: 0.05em;
    text-transform: uppercase;
    background: linear-gradient(180deg, var(--quote-top) 0%, var(--quote-bottom) 100%);
    -webkit-background-clip: text;
    background-clip: text;
    color: transparent;
  }
  .post__author {
    position: absolute;
    left: 0;
    right: 0;
    top: 893px;
    margin: 0;
    text-align: center;
    font-family: "Raleway", "Helvetica Neue", sans-serif;
    font-weight: 200;
    font-size: 50px;
    letter-spacing: 0.42em;
    padding-left: 0.42em;
    color: var(--author);
  }
</style>
</head>
<body>
  <main class="post">
    <div class="post__photo" role="img" aria-label="Blue-toned photograph of three women dancing in casual tops and jeans"></div>
    <p class="post__quote">The natural<br>healing within<br>each of us is<br>the greatest<br>force in getting<br>well.</p>
    <p class="post__author">MERIDOCLES</p>
  </main>
</body>
</html>
```